Infectious Diseases Research Laboratory Needs Business Card

We need a business card for an academic research laboratory based in Kansas City called MORVEK. The full lab name is Microbial Dose-Response/Exposure Bridging Studies Laboratory, but this does not need to be incorporated. We study novel ways to optimize the treatment of multidrug-resistant bacterial infections ("superbugs") throughout the entire biomedical research spectrum (from benchtop to bedside). The name MORVEK is not only an acronym for our lab name, but also represents our desire to make discoveries and explore the unknown (the stars, if you well). It also serves as an ode to the state of Kansas motto where we are based, ad astra per aspera ("to the stars, through difficulty").

Target Market(s)

Pharmaceutical companies, researchers

Industry/Entity Type

Pharmaceutical

Contact Information for Business Card

The business card should incorporate and complement our new logo (see uploaded files). Double-sided designs are preferred. Looking for something modern, but professional.

Font styles to use
Sans Serif

Requirements
Must have
• Double-sided. One side would ideally be a solid color incorporating logo and the other should also have the logo (smaller), but incorporate staff information.
• Color codes:
• Red: #F04C51
• Blue: #3477B5
• Gray: #808285

```html
<!DOCTYPE html>
<html lang="en">
<head>
<meta charset="utf-8">
<title>MORVEK Business Card</title>
<link href="https://fonts.googleapis.com/css2?family=Roboto:wght@400;500;700&display=swap" rel="stylesheet">
<style>
  :root{
    --red:#F04C51;
    --blue:#3477B5;
    --gray:#808285;
    --ink:#2b2b2b;
    --card-dark:#262727;
    --card-light:#ffffff;
    --backdrop:#ececec;
  }
  *{box-sizing:border-box;margin:0;padding:0}
  html,body{width:1200px;height:576px;overflow:hidden}
  body{background:var(--backdrop);font-family:"Roboto",Arial,sans-serif;position:relative}
  .card{position:absolute;top:140px;width:484px;height:294px;border-radius:14px;overflow:hidden;box-shadow:0 3px 8px rgba(0,0,0,.25)}
  .card--front{left:82px;background:var(--card-dark)}
  .card--back{left:618px;background:var(--card-light)}

  .wordmark{display:flex;align-items:center;gap:12px}
  .wordmark__dot{border-radius:50%;background:var(--red);flex:none}
  .wordmark__name{font-weight:500;color:var(--red);letter-spacing:2px;line-height:1}
  .wordmark__tagline{font-size:6px;letter-spacing:.8px;color:var(--gray);text-transform:uppercase;margin-top:3px;border-bottom:1px solid var(--gray);padding-bottom:2px;white-space:nowrap}

  .card--front .wordmark{position:absolute;left:80px;top:118px}
  .card--front .wordmark__dot{width:64px;height:64px}
  .card--front .wordmark__name{font-size:60px}

  .card--back .wordmark{position:absolute;left:24px;top:34px;gap:10px}
  .card--back .wordmark__dot{width:60px;height:60px}
  .card--back .wordmark__name{font-size:54px}

  .staff{position:absolute;left:24px;top:131px}
  .staff__name{font-size:20px;font-weight:700;color:var(--red)}
  .staff__role{font-size:12px;color:var(--ink);margin-left:8px}
  .staff__address{margin-top:12px;font-size:14px;line-height:18px;color:var(--ink)}

  .wave{position:absolute;left:0;top:0}

  .contact{position:absolute;right:14px;top:216px;list-style:none;text-align:right}
  .contact li{font-size:13px;line-height:18px;color:#fff;display:flex;justify-content:flex-end;align-items:center;gap:6px}
  .contact svg{width:11px;height:11px;fill:#fff}
</style>
</head>
<body>

<section class="card card--front">
  <div class="wordmark">
    <span class="wordmark__dot"></span>
    <div>
      <div class="wordmark__name">MORVEK</div>
      <div class="wordmark__tagline">Microbial Dose-Response/Exposure Bridging Studies Laboratory</div>
    </div>
  </div>
</section>

<section class="card card--back">
  <div class="wordmark">
    <span class="wordmark__dot"></span>
    <div>
      <div class="wordmark__name">MORVEK</div>
      <div class="wordmark__tagline">Microbial Dose-Response/Exposure Bridging Studies Laboratory</div>
    </div>
  </div>

  <div class="staff">
    <span class="staff__name">Dana Whitfield</span><span class="staff__role">Managing Director</span>
    <p class="staff__address">48 Harlow Avenue,<br>Kansas City 64108</p>
  </div>

  <svg class="wave" width="484" height="294" viewBox="0 0 484 294">
    <path d="M0,222 C90,250 200,258 300,232 C210,270 90,266 0,252 Z" fill="var(--blue)"/>
    <path d="M0,244 C130,278 270,236 370,186 C420,166 455,160 484,160 L484,294 L0,294 Z" fill="var(--red)"/>
    <path d="M42,236 C160,258 300,196 380,160 C430,140 460,140 484,140" fill="none" stroke="var(--gray)" stroke-width="6"/>
  </svg>

  <ul class="contact">
    <li>1800-555-0147
      <svg viewBox="0 0 24 24"><path d="M6.6 10.8a15.1 15.1 0 0 0 6.6 6.6l2.2-2.2a1 1 0 0 1 1-.25 11.4 11.4 0 0 0 3.6.6 1 1 0 0 1 1 1V20a1 1 0 0 1-1 1A17 17 0 0 1 3 4a1 1 0 0 1 1-1h3.5a1 1 0 0 1 1 1c0 1.25.2 2.45.6 3.6a1 1 0 0 1-.25 1z"/></svg></li>
    <li>www.morveklab.org
      <svg viewBox="0 0 24 24"><path d="M12 2a10 10 0 1 0 0 20 10 10 0 0 0 0-20zm6.9 6h-3a15.6 15.6 0 0 0-1.4-3.6A8 8 0 0 1 18.9 8zM12 4a14 14 0 0 1 1.9 4h-3.8A14 14 0 0 1 12 4zM4.3 14a8 8 0 0 1 0-4h3.4a16 16 0 0 0 0 4zm.8 2h3a15.6 15.6 0 0 0 1.4 3.6A8 8 0 0 1 5.1 16zm3-8h-3a8 8 0 0 1 4.4-3.6A15.6 15.6 0 0 0 8.1 8zM12 20a14 14 0 0 1-1.9-4h3.8A14 14 0 0 1 12 20zm2.3-6H9.7a14.6 14.6 0 0 1 0-4h4.6a14.6 14.6 0 0 1 0 4zm.2 5.6a15.6 15.6 0 0 0 1.4-3.6h3a8 8 0 0 1-4.4 3.6zm1.8-5.6a16 16 0 0 0 0-4h3.4a8 8 0 0 1 0 4z"/></svg></li>
    <li>dana@morveklab.org
      <svg viewBox="0 0 24 24"><path d="M2 5h20v14H2zm2 2v.5l8 5 8-5V7zm0 2.8V17h16V9.8l-8 5z"/></svg></li>
  </ul>
</section>

</body>
</html>
```